Technical Communications firm needs an article turned into a white paper

We want to redesign a 3-part blog series into a white paper that we can print for a conference. I've consolidated the three posts into the attached Word document.

We are looking for a light, easy to read design. Good use of graphics to support the message. I've added the graphics we used in the original post.

You can view them at
http://www.quillmarrowgroup.com/blog/are-you-satisfied-with-your-dita-solution/

Target Market(s)

Product managers from High-tech, Finance, and Medical industries.

Industry/Entity Type

Information Technology

Colors

Designer to choose colors to be used in the design.

Requirements
Must have
• Must be modern, light, easy to read and slick design. Try to incorporate the graphics provided, but feel free to add more. Must retain the lists and tables.
• Must align with our website/brand.
• Must be easy to read. So not too busy.
• Please move all footnotes to endnotes. You'll need to rework the numbering.
Nice to have
• Awesome coverpage.
Should not have
• Hokey clipart. Not too heavy or hard to read.

```html
<!DOCTYPE html>
<html lang="en">
<head>
<meta charset="utf-8">
<title>Are You Satisfied With Your DITA Solution? – White Paper Spread</title>
<link href="https://fonts.googleapis.com/css2?family=Montserrat:wght@500;600;700&family=Open+Sans:ital,wght@0,400;0,600;1,400&display=swap" rel="stylesheet">
<style>
  :root {
    --backdrop: #c9c7c2;
    --paper: #ffffff;
    --paper-shade: #f1f2f3;
    --sky: #4a9bd3;
    --navy: #2a2d6e;
    --ink: #4a4a4a;
    --muted: #7a7a7a;
    --chalk-board: #4b545b;
    --teal: #5aa58a;
    --lime: #9fc25a;
    --mustard: #d6ab2c;
  }
  * { box-sizing: border-box; margin: 0; padding: 0; }
  html, body { width: 1200px; height: 804px; overflow: hidden; }
  body {
    background: var(--backdrop);
    font-family: "Open Sans", sans-serif;
    color: var(--ink);
    position: relative;
  }
  .spread {
    position: absolute; left: 60px; top: 20px;
    width: 1080px; height: 764px;
    display: flex;
    box-shadow: 0 6px 20px rgba(0,0,0,.18);
  }
  .page {
    position: relative; width: 540px; height: 764px;
    background: linear-gradient(180deg, var(--paper) 0%, var(--paper) 70%, var(--paper-shade) 100%);
    overflow: hidden;
  }
  .page--left { border-right: 1px solid #e2e2e2; }
  .corner-tab {
    position: absolute; top: 0; width: 110px; height: 32px;
    background: var(--sky);
  }
  .page--left .corner-tab { left: 0; border-bottom-right-radius: 60px 32px; }
  .page--right .corner-tab { right: 0; border-bottom-left-radius: 60px 32px; }
  .cover-photo {
    position: absolute; left: 0; top: 0; width: 540px; height: 400px;
    background: radial-gradient(ellipse at 70% 60%, #5a636a 0%, var(--chalk-board) 55%, #3f474d 100%);
  }
  .page--left .corner-tab { z-index: 2; }
  .title {
    position: absolute; left: 42px; top: 428px; width: 460px;
    font-family: "Montserrat", sans-serif; font-weight: 700;
    font-size: 25px; line-height: 1.5; letter-spacing: -0.5px;
    text-transform: uppercase; color: var(--navy);
  }
  .title .accent { color: var(--sky); }
  .byline {
    position: absolute; left: 42px; top: 518px;
    font-style: italic; font-size: 12px; color: var(--ink);
  }
  .byline-role {
    position: absolute; left: 42px; top: 540px;
    font-style: italic; font-size: 8.5px; color: var(--muted);
  }
  .body-copy {
    position: absolute; left: 42px; top: 566px; width: 458px;
    font-size: 8.6px; line-height: 1.65; color: var(--ink);
  }
  .body-copy p + p { margin-top: 7px; }
  .footer {
    position: absolute; left: 0; bottom: 0; width: 540px; height: 86px;
  }
  .footer-band {
    position: absolute; left: 0; bottom: 0; width: 100%; height: 9px;
    background: var(--sky);
  }
  .brand {
    display: flex; align-items: center; gap: 6px;
    font-family: "Montserrat", sans-serif; font-weight: 700;
    font-size: 12px; line-height: 1.05; color: var(--navy);
    text-transform: uppercase;
  }
  .brand-dot { width: 20px; height: 20px; border-radius: 50%; background: var(--sky); flex: none; }
  .contact {
    font-size: 5.8px; line-height: 1.45; color: var(--muted);
  }
  .contact strong { color: var(--sky); font-weight: 600; display: block; }
  .page--left .brand { position: absolute; left: 34px; top: 24px; }
  .page--left .contact--web { position: absolute; left: 170px; top: 30px; }
  .page--left .contact--support { position: absolute; left: 270px; top: 22px; }
  .page--left .contact--office { position: absolute; left: 400px; top: 16px; }

  .page--right .content { position: absolute; left: 46px; top: 120px; width: 450px; }
  .section-heading {
    font-family: "Montserrat", sans-serif; font-weight: 600;
    font-size: 16px; color: var(--sky); margin-bottom: 6px;
  }
  .lede { font-size: 8.2px; line-height: 1.6; color: var(--ink); }
  .categories {
    display: flex; gap: 22px; margin: 16px 0 12px 40px; align-items: flex-start;
  }
  .category { text-align: center; width: 80px; }
  .category:nth-child(1) { margin-top: 28px; }
  .category:nth-child(2) { margin-top: 14px; }
  .category-box {
    height: 30px; display: flex; align-items: center; justify-content: center;
    font-family: "Montserrat", sans-serif; font-weight: 700; font-size: 12px; color: #fff;
  }
  .category--skills .category-box { background: var(--teal); }
  .category--tech .category-box { background: var(--lime); }
  .category--mgmt .category-box { background: var(--mustard); }
  .category-label { font-size: 7.5px; color: var(--ink); margin-top: 8px; }
  .note { font-size: 8.2px; line-height: 1.6; margin: 10px 0 26px; }
  .parts { list-style: none; margin-top: 12px; }
  .parts li { margin-bottom: 16px; }
  .part-title {
    font-family: "Montserrat", sans-serif; font-weight: 600; font-size: 10px; color: var(--navy);
  }
  .part-title span { color: var(--sky); }
  .part-text { font-size: 8.2px; line-height: 1.6; margin-top: 5px; }
  .page--right .brand { position: absolute; right: 36px; top: 0; }
  .page--right .contact--office { position: absolute; left: 46px; top: 30px; }
  .page--right .contact--support { position: absolute; left: 140px; top: 26px; }
  .page--right .contact--web { position: absolute; left: 260px; top: 22px; }
</style>
</head>
<body>
<main class="spread">
  <section class="page page--left">
    <div class="corner-tab"></div>
    <div class="cover-photo" role="img" aria-label="Photo of a bearded man looking doubtful in front of a chalkboard with rows of yellow chalk rating stars and tick boxes"></div>
    <h1 class="title"><span class="accent">Are you satisfied</span> with your DITA solution?</h1>
    <p class="byline">By Dana Whitlock</p>
    <p class="byline-role">President of Quill Marrow Authoring Group Inc.</p>
    <div class="body-copy">
      <p>If your answer is “No” then you are not alone according to a 2017 survey of more than 250 technical communication professionals conducted by The Docs Drover. The DITA Satisfaction Survey[i] indicates that 62% of respondents using DITA are—to varying degrees—dissatisfied. As many as 10% of that group were very dissatisfied reporting that their DITA implementation is experiencing ‘big’ challenges. It’s not surprising that there’s significant dissatisfaction amongst those who have adopted DITA. After all, moving to DITA is a seismic shift in technical writing; a big change with many opportunities for things to go wrong.</p>
      <p>The good news is that most DITA users don’t see their problems as insurmountable. Many just need a little help getting to where they’d like to be.</p>
    </div>
    <footer class="footer">
      <div class="brand"><span class="brand-dot"></span><span>Quill Marrow<br>Group</span></div>
      <div class="contact contact--web">hello@quillmarrowgroup.com<br>www.quillmarrowgroup.com</div>
      <div class="contact contact--support"><strong>Technical Support</strong>Call: +1 (555) 014-2730, Press 1#<br>email: help@quillmarrowgroup.com</div>
      <div class="contact contact--office"><strong>Head Office</strong>48 Lantern Row 3rd Floor<br>Brookhaven, Ontario<br>K0A 1B2 Canada</div>
      <div class="footer-band"></div>
    </footer>
  </section>

  <section class="page page--right">
    <div class="corner-tab"></div>
    <div class="content">
      <h2 class="section-heading">Breakdown of the issues</h2>
      <p class="lede">The Docs Drover DITA Satisfaction Survey asked respondents to rank the top 10 issues facing DITA users. These issues fit into three major categories including</p>
      <div class="categories">
        <div class="category category--skills"><div class="category-box">01</div><p class="category-label">Skills Development</p></div>
        <div class="category category--tech"><div class="category-box">02</div><p class="category-label">Technology</p></div>
        <div class="category category--mgmt"><div class="category-box">03</div><p class="category-label">Management</p></div>
      </div>
      <p class="note">The DITA Satisfaction Survey Aggregate Results revealed little spread between the ranking of the issues indicating that respondents likely faced more than one issue of concern.</p>
      <h2 class="section-heading">In this article</h2>
      <p class="lede">In this article, we examine three issues impacting DITA satisfaction to help you find the best place to start making improvements.</p>
      <ol class="parts">
        <li><p class="part-title">1. Part-1: <span>Skills Development</span></p><p class="part-text">This problem area is far and away the most pressing obstacle for a successful DITA deployment. Too often authors are left to figure out how to adapt to writing for DITA on their own.</p></li>
        <li><p class="part-title">2. Part-2: <span>Technology</span></p><p class="part-text">We often hear about the failure of the technology as it relates to performance or complexity. While technology may seem the most likely culprit, it is often not the root cause of the problem.</p></li>
        <li><p class="part-title">3. Part-3: <span>Management</span></p><p class="part-text">While these issues appear to be of least concern to many survey respondents, they are most likely to form the root cause of all other issues identified in the survey. This points to a general lack of awareness as to the role management should be playing in collaborative, structured authoring solutions.</p></li>
      </ol>
    </div>
    <footer class="footer">
      <div class="brand"><span class="brand-dot"></span><span>Quill Marrow<br>Group</span></div>
      <div class="contact contact--office"><strong>Head Office</strong>48 Lantern Row 3rd Floor<br>Brookhaven, Ontario<br>K0A 1B2 Canada</div>
      <div class="contact contact--support"><strong>Technical Support</strong>Call: +1 (555) 014-2730, Press 1#<br>email: help@quillmarrowgroup.com</div>
      <div class="contact contact--web">hello@quillmarrowgroup.com<br>www.quillmarrowgroup.com</div>
      <div class="footer-band"></div>
    </footer>
  </section>
</main>
</body>
</html>
```